Cardiologist needs a unique and unforgettable business card design

Hi, I am a Cardiologist (heart specialist) and I need a business card as I am starting out my own practice very soon.
I have so used to seeing very boring and forgettable business cards that people take one look and then it goes into the bin.
I hope you can design one card that tells people immediately that it is from a Cardiologist (Heart Specialist) who is good, experienced, mature and save lives.
My colours that I like are green/white/earthly tones but I am also open to various colours combinations.
My clinic name is called Veyla Cardiology and I am attaching the Logo and information needed on the name card for you.
I would like the definition of Veyla to be in the name card
Veyla - To save one suffering from disease, to make well, heal, preserve,
restore to health and to make whole one again
I would like to have Spot UV or Embossing or Both to make the card stand out.
Thank you very much
Clinic

```html
<!DOCTYPE html>
<html lang="en">
<head>
<meta charset="utf-8">
<title>Veyla Cardiology – Business Card</title>
<link rel="stylesheet" href="https://fonts.googleapis.com/css2?family=Lato:wght@400;700&family=Open+Sans:wght@400;600;700&family=Noto+Sans+SC:wght@500&display=swap">
<style>
  :root {
    --brand-red: #b3202c;
    --forest: #1f4d33;
    --forest-deep: #153a27;
    --scene-top: #2c5e45;
    --scene-bottom: #143826;
    --paper: #ffffff;
    --ink: #1a1a1a;
    --ink-soft: #3c3c3c;
    --band-text: #e6efe9;
  }
  * { box-sizing: border-box; margin: 0; padding: 0; }
  html, body { width: 1200px; height: 1000px; overflow: hidden; }
  body {
    font-family: "Open Sans", Arial, sans-serif;
    background: var(--paper);
    color: var(--ink);
    position: relative;
  }

  /* Identity header */
  .identity {
    height: 216px;
    display: flex;
    align-items: center;
    justify-content: center;
    gap: 26px;
  }
  .identity__name {
    font-family: "Lato", Arial, sans-serif;
    font-weight: 700;
    font-size: 62px;
    letter-spacing: 4px;
    color: var(--ink);
  }
  .identity__tagline {
    font-family: "Lato", Arial, sans-serif;
    font-weight: 700;
    font-size: 17px;
    letter-spacing: 1.5px;
    color: var(--ink);
    align-self: flex-end;
    margin-bottom: 80px;
  }

  /* Presentation area */
  .stage {
    position: absolute;
    top: 216px; left: 0;
    width: 1200px; height: 784px;
    background: linear-gradient(160deg, var(--scene-top), var(--scene-bottom));
    display: flex;
    align-items: center;
    justify-content: center;
    gap: 60px;
  }

  /* Card */
  .card {
    width: 500px;
    height: 290px;
    background: var(--paper);
    position: relative;
    overflow: hidden;
    box-shadow: 0 14px 30px rgba(0,0,0,.35);
  }
  .card__brand {
    position: absolute;
    top: 22px; left: 26px;
    display: flex; align-items: baseline; gap: 10px;
  }
  .card__wordmark {
    font-family: "Lato", Arial, sans-serif;
    font-weight: 700;
    font-size: 24px;
    letter-spacing: 3px;
    color: var(--ink);
  }
  .card__tagline {
    font-family: "Lato", Arial, sans-serif;
    font-size: 8.5px;
    letter-spacing: .8px;
    color: var(--ink-soft);
  }
  .card__rule {
    position: absolute;
    left: 26px; right: 0;
    height: 1px;
    background: var(--forest);
  }
  .card__rule::before {
    content: "";
    position: absolute;
    left: -3px; top: -3px;
    width: 7px; height: 7px;
    border-radius: 50%;
    background: var(--forest);
  }
  .card__body { position: absolute; left: 26px; right: 26px; }
  .card__band {
    position: absolute;
    left: 0; right: 0; bottom: 0;
    height: 88px;
    background: var(--forest);
    color: var(--band-text);
    padding: 16px 26px;
    font-size: 9.5px;
    line-height: 1.6;
  }

  /* Front */
  .doctor__name {
    font-family: "Open Sans", Arial, sans-serif;
    font-weight: 700;
    font-size: 17px;
    color: var(--forest);
    letter-spacing: .5px;
  }
  .doctor__name-local {
    font-family: "Noto Sans SC", "Open Sans", sans-serif;
    font-weight: 500;
    font-size: 14px;
    color: var(--forest);
  }
  .doctor__role {
    font-family: "Lato", Arial, sans-serif;
    font-weight: 700;
    font-size: 9.5px;
    letter-spacing: 1.6px;
    text-transform: uppercase;
    color: var(--forest);
    margin-top: 3px;
  }
  .doctor__role-local {
    font-family: "Noto Sans SC", "Open Sans", sans-serif;
    font-size: 9px;
    color: var(--forest);
  }
  .doctor__credentials {
    font-size: 8.5px;
    color: var(--ink-soft);
    line-height: 1.5;
    margin-top: 3px;
  }
  .band__mark {
    font-family: "Lato", Arial, sans-serif;
    font-weight: 700;
    font-size: 15px;
    letter-spacing: 2px;
    color: var(--band-text);
    margin-bottom: 4px;
  }
  .band__definition { font-style: italic; max-width: 400px; }

  /* Back */
  .hours__title {
    font-family: "Lato", Arial, sans-serif;
    font-weight: 700;
    font-size: 11px;
    letter-spacing: 1.4px;
    text-transform: uppercase;
    color: var(--forest);
    margin-bottom: 4px;
  }
  .hours__list { list-style: none; font-size: 10px; line-height: 1.65; color: var(--ink-soft); }
</style>
</head>
<body>

<header class="identity">
  <span class="identity__name">Veyla Cardiology</span>
  <span class="identity__tagline">Saving hearts • Saving lives</span>
</header>

<main class="stage">

  <!-- Front of card -->
  <article class="card card--front">
    <div class="card__brand">
      <span class="card__wordmark">Veyla Cardiology</span>
    </div>
    <div class="card__rule" style="top:62px"></div>
    <div class="card__body" style="top:72px">
      <p class="doctor__name">DR LIM KAI WEN <span class="doctor__name-local">(林凯文医生)</span></p>
      <p class="doctor__role">Consultant General &amp; Interventional Cardiologist</p>
      <p class="doctor__role-local">心脏及介入性心脏专科医生</p>
      <p class="doctor__credentials">MBBS (S'pore), MRCP (United Kingdom), FRCP (Edinburgh),<br>FACC (USA), FAMS (Cardiology), ACSM (Clinical Exercise Physiologist, USA)</p>
    </div>
    <div class="card__band">
      <p class="band__mark">Veyla</p>
      <p class="band__definition">To save one suffering from disease, to make well, heal, preserve, restore to health and to make whole one again</p>
    </div>
  </article>

  <!-- Back of card -->
  <article class="card card--back">
    <div class="card__brand">
      <span class="card__wordmark">Veyla Cardiology</span>
    </div>
    <p class="card__tagline" style="position:absolute;top:54px;left:26px">Saving hearts • Saving lives</p>
    <div class="card__rule" style="top:76px"></div>
    <div class="card__body" style="top:90px">
      <p class="hours__title">Consultation Hours</p>
      <ul class="hours__list">
        <li>Monday to Friday : 9am to 1pm, 2pm to 5pm</li>
        <li>Saturday : 9am to 1pm</li>
        <li>Sunday and Public Holidays : Closed</li>
      </ul>
    </div>
    <div class="card__band">
      <p>Address : Harbourview Specialist Centre<br>12 Calloway Road #04-21 Singapore 308412</p>
      <p>Email : drlimkaiwen@veylacardiology.com</p>
      <p>Website : www.veylacardiology.com</p>
    </div>
  </article>

</main>
</body>
</html>
```